District Manager Business Card

Hello, I own 3 automotive repair shops that are all 3 different names. I need a card that has all 3 locations and logos on it. Just a simple, modern, clean design. I selected double sided, but If a single side is more ideal, thats ok too. I am open to explore both options. I attached the 3 logos in a few different formats.

Industry/Entity Type

Auto Repair

Contact Information for Business Card

Requirements
Must have
• Location information:
Q&L Automotive
482 Birchfield Ave.
Ashbury TN 38190

MOTO MEND
257 Pine Hollow Turnpike
Fenwick TN 37012

Brantmoor Tire & Auto
614 North Aspen Ave.
Brantmoor TN 38402

District Manager - Dale Hobart - Dale@qandlauto-example.com - Cell: 555-555-0196
Nice to have
• This can be a single or a double sided card. Just want a clean card that shows all 3 locations.

```html
<!DOCTYPE html>
<html lang="en">
<head>
<meta charset="utf-8">
<title>Dale Hobart – District Manager Business Card</title>
<link rel="stylesheet" href="https://fonts.googleapis.com/css2?family=Montserrat:wght@400;600&family=Gentium+Book+Plus&display=swap">
<style>
  :root {
    --page-bg: #dfe3e8;
    --card-top: #f4f5f7;
    --card-bottom: #dde5ee;
    --brand-red: #b5161d;
    --brand-red-light: #c43a41;
    --ink: #262626;
    --ink-soft: #444a52;
    --band: #141414;
    --white: #ffffff;
    --badge-blue: #2f3b86;
  }
  * { margin: 0; padding: 0; box-sizing: border-box; }
  html, body {
    width: 1200px; height: 900px; overflow: hidden;
    background: var(--page-bg);
  }
  .business-card {
    position: absolute; left: 75px; top: 150px;
    width: 1050px; height: 600px;
    background: linear-gradient(180deg, var(--card-top) 0%, #eef0f3 55%, var(--card-bottom) 100%);
    box-shadow: 0 18px 40px rgba(0,0,0,.18);
    overflow: hidden;
    font-family: "Montserrat", sans-serif;
    color: var(--ink);
  }
  .name-panel {
    position: absolute; left: 600px; top: 0;
    width: 450px; height: 172px;
    background: linear-gradient(90deg, var(--brand-red) 0%, var(--brand-red-light) 100%);
    border-bottom-left-radius: 8px;
    color: var(--white);
    text-align: right;
    padding: 56px 63px 0 0;
  }
  .person-name { font-weight: 600; font-size: 40px; letter-spacing: 2px; line-height: 1; }
  .person-title { font-weight: 400; font-size: 26px; letter-spacing: .5px; margin-top: 10px; line-height: 1; }

  .contact-list {
    position: absolute; left: 53px; top: 192px;
    list-style: none;
    font-family: "Gentium Book Plus", serif;
    font-size: 26px; color: var(--ink);
  }
  .contact-item { display: flex; align-items: center; height: 37px; }
  .contact-icon { width: 28px; height: 28px; margin-right: 23px; fill: var(--ink); }

  .section-rule {
    position: absolute; left: 0; top: 334px;
    width: 100%; height: 4px; background: var(--ink);
  }
  .locations {
    position: absolute; left: 0; top: 338px;
    width: 100%; height: 236px;
    display: grid; grid-template-columns: 356px 336px 358px;
    background: rgba(190, 208, 228, .25);
  }
  .location { text-align: center; padding-top: 42px; }
  .shop-mark {
    height: 50px; display: flex; align-items: center; justify-content: center; gap: 10px;
    font-weight: 600; font-size: 22px; color: var(--badge-blue);
  }
  .shop-mark.dark { color: var(--ink); }
  .mark-square { width: 16px; height: 16px; background: currentColor; }
  .mark-circle { width: 18px; height: 18px; border-radius: 50%; background: currentColor; }
  .shop-name { font-weight: 600; font-size: 23px; margin-top: 24px; color: var(--ink); }
  .shop-name .accent { color: var(--brand-red); font-weight: 400; }
  .shop-address { font-size: 22px; color: var(--ink-soft); line-height: 33px; margin-top: 2px; }

  .base-band {
    position: absolute; left: 0; bottom: 0;
    width: 100%; height: 26px;
    background: linear-gradient(180deg, #2a2a2a 0%, var(--band) 100%);
  }
</style>
</head>
<body>
  <article class="business-card">
    <header class="name-panel">
      <div class="person-name">DALE HOBART</div>
      <div class="person-title">District Manager</div>
    </header>

    <ul class="contact-list">
      <li class="contact-item">
        <svg class="contact-icon" viewBox="0 0 28 28" aria-hidden="true">
          <path d="M8 2h12a2 2 0 0 1 2 2v20a2 2 0 0 1-2 2H8a2 2 0 0 1-2-2V4a2 2 0 0 1 2-2zm1 4v15h10V6zm5 16.5a1 1 0 1 0 0 .01z"/>
        </svg>
        555-555-0196
      </li>
      <li class="contact-item">
        <svg class="contact-icon" viewBox="0 0 28 28" aria-hidden="true">
          <path d="M2 7h24v15H2zm2 2v.6l10 6.6 10-6.6V9zm0 3v8h20v-8l-10 6.6z"/>
        </svg>
        Dale@qandlauto-example.com
      </li>
      <li class="contact-item">
        <svg class="contact-icon" viewBox="0 0 28 28" aria-hidden="true">
          <circle cx="14" cy="14" r="12"/>
          <path d="M7 9c3 0 4 2 3 4s1 3 2 5-1 4-2 5M18 4c-1 3 1 4 3 4s3 3 2 5" fill="none" stroke="#f4f5f7" stroke-width="2"/>
        </svg>
        www.qandlauto-example.com
      </li>
    </ul>

    <div class="section-rule"></div>

    <section class="locations">
      <div class="location">
        <div class="shop-mark"><span class="mark-square"></span>Q&amp;L Automotive</div>
        <div class="shop-name">Q&amp;L Automotive</div>
        <div class="shop-address">482 Birchfield Ave.<br>Ashbury TN 38190</div>
      </div>
      <div class="location">
        <div class="shop-mark dark">MOTO MEND</div>
        <div class="shop-name"><span class="accent">MOTO</span> MEND</div>
        <div class="shop-address">257 Pine Hollow Turnpike<br>Fenwick TN 37012</div>
      </div>
      <div class="location">
        <div class="shop-mark dark"><span class="mark-circle"></span>Brantmoor Tire &amp; Auto</div>
        <div class="shop-name">Brantmoor Tire &amp; Auto</div>
        <div class="shop-address">614 North Aspen Ave.<br>Brantmoor TN 38402</div>
      </div>
    </section>

    <div class="base-band"></div>
  </article>
</body>
</html>
```